International Wine events organiser seeks simple but stunning business card

I am a freelance events, marketing and PR provider specialised in the Wine industry. I help wineries and wine regions reach trade and consumers in foreign markets through events, help with the websites and communications, press trips and promotional activities. I am looking for a business card which is simple yet effective and is linked to events and communication.

I work mainly - but exclusively - with Italian wineries organising events for them in foreign market.s

I would like to use red in the logo as my present website (lunabrendor.com) used grey and red (although I will be changing the design at a later date).

Target Market(s)

Wine producers, promotional bodies in wine sector, companies looking to hire event organisers,

Industry/Entity Type

Marketing

Requirements
Must have
• My Name - Luna Brendor
My address
My phone
My website : www.lunabrendor.com
my Blog : pebbleandtwig.me

Should not have
• Butterflies, stars, flowers, anything not particularly linked to wine - would like to keep it simple, modern and eye-catching without being too cliche.

```html
<!DOCTYPE html>
<html lang="en">
<head>
<meta charset="utf-8">
<title>Luna Brendor – Business Card</title>
<link rel="stylesheet" href="https://fonts.googleapis.com/css2?family=Fira+Sans:ital,wght@1,400;1,600&display=swap">
<style>
  :root {
    --paper: #ffffff;
    --edge: #222222;
    --wine: #7a1244;
    --ink: #1a1a1a;
    --leaf: #e6e6e6;
    --grape: #b77d98;
    --grape-deep: #9a5a78;
  }
  html, body {
    margin: 0;
    padding: 0;
    overflow: hidden;
    background: var(--paper);
  }
  .card {
    position: relative;
    width: 777px;
    height: 1200px;
    box-sizing: border-box;
    border: 1px solid var(--edge);
    background: var(--paper);
    overflow: hidden;
    font-family: "Fira Sans", "Optima", sans-serif;
    font-style: italic;
  }
  .art {
    position: absolute;
    left: 0;
    top: 0;
    width: 777px;
    height: 1200px;
  }
  .card-name {
    position: absolute;
    left: 237px;
    top: 182px;
    margin: 0;
    font-size: 52px;
    font-weight: 600;
    line-height: 1;
    color: var(--wine);
    white-space: nowrap;
  }
  .line {
    position: absolute;
    left: 237px;
    margin: 0;
    font-size: 44px;
    font-weight: 400;
    line-height: 1;
    color: var(--ink);
    white-space: nowrap;
  }
  .line--web { font-weight: 600; }
  .line--street { top: 612px; }
  .line--city   { top: 675px; }
  .line--phone  { top: 766px; }
  .line--email  { top: 831px; }
  .line--web    { top: 960px; }
  .line--blog   { top: 1026px; }
</style>
</head>
<body>
<div class="card">
  <svg class="art leaf-art" role="img" aria-label="Faint grey grape leaf and vine silhouette" viewBox="0 0 777 1200">
    <defs>
      <radialGradient id="leafTone" cx="0.5" cy="0.5" r="0.5">
        <stop offset="0" stop-color="var(--leaf)"/>
        <stop offset="0.7" stop-color="var(--leaf)"/>
        <stop offset="1" stop-color="var(--leaf)" stop-opacity="0"/>
      </radialGradient>
    </defs>
    <ellipse cx="400" cy="560" rx="400" ry="430" fill="url(#leafTone)"/>
  </svg>

  <svg class="art grape-art" role="img" aria-label="Translucent wine-red grape cluster running down the left edge" viewBox="0 0 777 1200">
    <defs>
      <linearGradient id="grapeTone" x1="0" y1="0" x2="1" y2="0">
        <stop offset="0" stop-color="var(--grape-deep)" stop-opacity="0.55"/>
        <stop offset="0.6" stop-color="var(--grape)" stop-opacity="0.35"/>
        <stop offset="1" stop-color="var(--grape)" stop-opacity="0"/>
      </linearGradient>
    </defs>
    <rect x="0" y="120" width="190" height="1080" fill="url(#grapeTone)"/>
  </svg>

  <h1 class="card-name">Luna Brendor</h1>

  <p class="line line--street">Lindenhofer Straße 12</p>
  <p class="line line--city">80469 Munich</p>
  <p class="line line--phone">Phone +49 1705550123</p>
  <p class="line line--email">luna@lunabrendor.com</p>
  <p class="line line--web">www.lunabrendor.com</p>
  <p class="line line--blog">Blog: pebbleandtwig.me</p>
</div>
</body>
</html>
```